Poster announcing University Web Analytics talk

We need a poster to announce an upcoming talk on Web Analytics at the local University. The event is addressed to final year students (mostly in Informatic Engineering, although other majors are wellcomed as well) who may be interested in specializing in this rising field.

The poster should present a brief list of the points we'll be addressing, as well as the place and time of the meeting. Also, it must feature our company logo (check the uploads section to find it) and our website url: http://www.brasslanternworks.net.

Texts for the poster:

Headline: "Get specialized in Web & Mobile Analytics"

Topics that will be covered:
- Introduction to Analytics, market, work opportunities
- Know the basics of an Analytics project: planning, phases, implementation
- Job bank: bring your CV!

Event information: "Thursday 20th June at the Escuela de Sistemas, Instituto Pelayo Norte". [A space to fill with the time must be provided here]

However, we'll be translating all the text to Spanish later, so we'll need a file where we can modify the text layers.
Updates

Thanks to all of you, we're receiving so many excellent works!

We had missed to include some important information on the brief - we didn't say anything about the colors, and we have been getting some designs based in dark colors. Now, it doesn't matter what colors you use, but we'd like better a brighter design (no matter if the color combination is more playful or either rather serious). This is going to be a free talk addressed to last year students, so we want to transmit a feeling of an interesting, easy and entertaining afternoon.

I hope these comments are helpful, please reach me with any question or comment. 

Thanks a lot again!
Nuria 
BL team

Target Market(s)

Final year students and graduates.

Industry/Entity Type

Bank

Requirements
Must have
• Design must be submitted in vector format, preferably .psd. We must be able to modify the text layers. Our logo (check the files section) and website url (http://www.brasslanternworks.net) must be included
Nice to have
• Illustrations making reference to Analytics (charts, statistics, code) and/or the internet will be a plus!

```html
<!DOCTYPE html>
<html lang="en">
<head>
<meta charset="utf-8">
<title>Get specialized in Web &amp; Mobile Analytics — Brass Lantern Works</title>
<link rel="stylesheet" href="https://fonts.googleapis.com/css2?family=Montserrat:wght@300;400;600;700&family=Open+Sans:wght@600;700&display=swap">
<style>
  :root {
    --navy: #1d3866;
    --navy-soft: #2c4c80;
    --sky-top: #e6edf7;
    --sky-mid: #c6d5ea;
    --sky-low: #8eaad0;
    --deep: #2e5893;
    --band: #bcd0ec;
    --white: #ffffff;
    --page: #f3f5f8;
    --green: #7cb342;
  }
  * { margin: 0; padding: 0; box-sizing: border-box; }
  html, body { width: 1200px; height: 1000px; overflow: hidden; background: var(--page); }
  body { position: relative; font-family: "Montserrat", Arial, sans-serif; color: var(--navy); }

  .poster {
    position: absolute; left: 285px; top: 55px; width: 630px; height: 885px;
    background: linear-gradient(180deg, var(--sky-top) 0%, var(--sky-mid) 45%, #d9e3f1 60%, var(--sky-low) 85%, var(--deep) 100%);
    overflow: hidden;
    box-shadow: 0 4px 18px rgba(30, 56, 102, 0.25);
  }
  .poster__frame {
    position: absolute; inset: 14px; border: 1px solid rgba(255,255,255,0.8); pointer-events: none; z-index: 5;
  }
  .poster__texture {
    position: absolute; left: 0; top: 0; width: 100%; height: 260px;
    background: linear-gradient(180deg, rgba(160,185,220,0.35), rgba(230,237,247,0));
  }
  .poster__wave { position: absolute; left: 0; bottom: 0; width: 100%; height: 420px; }

  .headline { position: absolute; left: 28px; top: 0; padding-left: 14px; border-left: 8px solid var(--navy); padding-top: 34px; height: 107px; }
  .headline__lead { display: block; font-weight: 400; font-size: 34px; line-height: 38px; letter-spacing: -0.5px; color: var(--navy); }
  .headline__main { display: block; font-weight: 700; font-size: 43px; line-height: 46px; letter-spacing: -0.6px; color: var(--navy); white-space: nowrap; }
  .headline__marker { position: absolute; left: 555px; top: 123px; }

  .topics {
    position: absolute; left: 48px; top: 178px; width: 529px; height: 161px;
    border: 1px solid var(--navy-soft);
    background: rgba(235, 241, 250, 0.45);
  }
  .topics__title {
    height: 30px; padding-left: 12px; line-height: 30px;
    background: linear-gradient(90deg, var(--band), rgba(188,208,236,0.2));
    font-family: "Open Sans", Arial, sans-serif; font-weight: 700; font-size: 15px; color: var(--navy);
    text-transform: uppercase;
  }
  .topics__chart { position: absolute; right: -2px; top: 34px; }
  .topics__list { list-style: none; position: relative; }
  .topics__item { position: absolute; font-family: "Open Sans", Arial, sans-serif; font-weight: 600; font-size: 15.5px; line-height: 18px; color: var(--navy); }
  .topics__item--1 { left: 34px; top: 14px; }
  .topics__item--2 { left: 52px; top: 40px; width: 460px; }
  .topics__item--3 { left: 52px; top: 92px; }
  .topics__links { position: absolute; left: 0; top: 30px; }

  .event { position: absolute; right: 58px; top: 393px; text-align: right; }
  .event__time { font-weight: 700; font-size: 54px; line-height: 50px; color: var(--navy); }
  .event__time small { font-size: 24px; font-weight: 700; margin-left: 2px; }
  .event__date { font-weight: 700; font-size: 21px; line-height: 28px; color: var(--navy); }
  .event__place { margin-top: 10px; font-weight: 400; font-size: 19px; line-height: 22px; color: var(--navy); }
  .event__venue { font-weight: 700; font-size: 21px; line-height: 26px; color: var(--navy); }

  .poster__url { position: absolute; left: 27px; bottom: 24px; font-size: 16px; color: var(--white); z-index: 6; }
  .poster__url b { font-weight: 700; }

  .brand {
    position: absolute; left: 370px; bottom: 3px; width: 222px; height: 95px; background: var(--white);
    display: flex; align-items: center; justify-content: center; gap: 10px; z-index: 6;
  }
  .brand__square { width: 16px; height: 16px; background: var(--navy-soft); }
  .brand__name { font-weight: 600; font-size: 20px; line-height: 22px; color: var(--navy-soft); }
</style>
</head>
<body>
  <article class="poster">
    <div class="poster__texture" role="img" aria-label="Faint binary code digits pattern"></div>

    <svg class="poster__wave" viewBox="0 0 630 420" role="img" aria-label="Wave of small pixel squares rising across the lower poster">
      <defs>
        <linearGradient id="waveFill" x1="0" y1="0" x2="0" y2="1">
          <stop offset="0" stop-color="#f4f7fc" stop-opacity="0.85"/>
          <stop offset="0.55" stop-color="#b7c9e4" stop-opacity="0.8"/>
          <stop offset="1" stop-color="#3a649e"/>
        </linearGradient>
      </defs>
      <path d="M0 120 C 90 60, 180 210, 320 230 C 430 245, 520 150, 630 70 L630 420 L0 420 Z" fill="url(#waveFill)"/>
    </svg>

    <div class="poster__frame"></div>

    <header class="headline">
      <span class="headline__lead">Get specialized in</span>
      <span class="headline__main">Web &amp; Mobile Analytics</span>
    </header>
    <svg class="headline__marker" width="42" height="16" viewBox="0 0 42 16" aria-hidden="true">
      <polygon points="0,0 42,0 21,16" fill="#1d3866"/>
    </svg>

    <section class="topics">
      <h2 class="topics__title">Topics that will be covered</h2>
      <svg class="topics__chart" width="150" height="110" viewBox="0 0 150 110" aria-hidden="true">
        <path d="M110 70 L110 0 A70 70 0 0 1 180 70 Z" fill="#c9dca6" opacity="0.5"/>
        <path d="M110 70 L40 70 A70 70 0 0 1 110 0 Z" fill="#a9c8e4" opacity="0.5"/>
        <path d="M110 70 L180 70 A70 70 0 0 1 40 70 Z" fill="#9fbde0" opacity="0.4"/>
      </svg>
      <svg class="topics__links" width="60" height="131" viewBox="0 0 60 131" aria-hidden="true">
        <g stroke="#1d3866" stroke-width="1.5" fill="none">
          <line x1="18" y1="23" x2="36" y2="48"/>
          <line x1="36" y1="48" x2="12" y2="79"/>
          <line x1="12" y1="79" x2="36" y2="109"/>
        </g>
        <g fill="#1d3866">
          <circle cx="18" cy="23" r="8"/>
          <circle cx="36" cy="48" r="5.5"/>
          <circle cx="12" cy="79" r="3"/>
          <circle cx="36" cy="109" r="9"/>
        </g>
      </svg>
      <ul class="topics__list">
        <li class="topics__item topics__item--1">Introduction to Analytics, market, work opportunities.</li>
        <li class="topics__item topics__item--2">Know the basics of an Analytics project: planning, phases, implementation.</li>
        <li class="topics__item topics__item--3">Job bank: BRING YOUR CV!</li>
      </ul>
    </section>

    <section class="event">
      <p class="event__time">9<small>am</small></p>
      <p class="event__date">Thursday, 20th June</p>
      <p class="event__place">at the Escuela de Sistemas</p>
      <p class="event__venue">Instituto Pelayo Norte</p>
    </section>

    <p class="poster__url">www.<b>brasslanternworks</b>.net</p>

    <div class="brand">
      <span class="brand__square"></span>
      <span class="brand__name">brass lantern<br>works</span>
    </div>
  </article>
</body>
</html>
```